Halvik Partners Building Business Cards

We need a business card that reflects our business as "Solar Experts" in San Diego. Browse our website www.halvikpartners.example our License needs to be displayed as "CSLB# 4871306" our phone number is (619) 482-5537

Save thousands on your electric bills and increase the value of your home while helping to protect the environment. Our solar installation experts will help you design the system that's right for you, using only the highest quality equipment that will look great and give you ideal performance. Our goal is to make you energy independent, and get your electric bill to 0.

Paul Ostrander
(619) 482-5537
paul@halvikpartners.example

Target Market(s)

Home owners in san diego looking for solar

Industry/Entity Type

Solar Energy

Contact Information for Business Card

Paul Ostrander
(619) 482-5537
paul@halvikpartners.example

Font styles to use
Other font styles liked:
• Use our logo font

Requirements
Must have
• License needs to be displayed as "CSLB# 4871306" our phone number is (619) 482-5537
Nice to have
• Real images of rooftop home solar in san diego
Should not have
• our business address

```html
<!DOCTYPE html>
<html lang="en">
<head>
<meta charset="utf-8">
<title>Halvik Partners Building – Business Cards</title>
<link href="https://fonts.googleapis.com/css2?family=Open+Sans:wght@400;600;700;800&display=swap" rel="stylesheet">
<style>
  :root {
    --navy: #1f3a78;
    --gold: #f5a800;
    --ink: #1c1c1c;
    --paper: #ffffff;
    --backdrop: #e6e4e0;
  }
  * { margin: 0; padding: 0; box-sizing: border-box; }
  html, body {
    width: 1200px; height: 900px; overflow: hidden;
    background: var(--backdrop);
    font-family: "Open Sans", Arial, sans-serif;
  }
  .card {
    position: absolute; left: 250px;
    width: 700px; height: 400px;
    background: var(--paper);
    box-shadow: 0 6px 18px rgba(0,0,0,.18);
    overflow: hidden;
  }
  .card--front { top: 40px; }
  .card--back  { top: 460px; }

  .wordmark {
    position: absolute;
    color: var(--navy);
    font-weight: 800;
    font-size: 46px;
    line-height: 1.05;
    letter-spacing: -0.5px;
  }
  .card--front .wordmark { left: 130px; top: 140px; width: 460px; }
  .card--back .wordmark  { left: 320px; top: 115px; width: 360px; font-size: 38px; }

  .corner-mark { position: absolute; left: 0; top: 18px; }

  .holder-name {
    position: absolute; left: 70px; top: 26px;
    font-size: 20px; font-weight: 700; color: var(--navy);
  }
  .holder-name .surname { color: var(--gold); }

  .contact {
    position: absolute; left: 40px; top: 215px;
    list-style: none; font-size: 17px; color: var(--ink);
  }
  .contact li { display: flex; align-items: center; gap: 10px; height: 28px; }
  .contact .label { color: var(--navy); font-weight: 700; }
  .contact .license { margin-left: 0; }
  .contact svg { flex: none; }

  .footer-bands { position: absolute; left: 0; bottom: 0; }
</style>
</head>
<body>

<section class="card card--front" aria-label="Card front">
  <div class="wordmark">Halvik Partners Building</div>
</section>

<section class="card card--back" aria-label="Card back">
  <svg class="corner-mark" width="60" height="36" viewBox="0 0 60 36" aria-hidden="true">
    <polygon points="0,0 40,0 10,36 0,36" fill="var(--navy)"/>
    <polygon points="44,0 60,0 60,36 14,36" fill="var(--gold)"/>
  </svg>
  <div class="holder-name">Paul <span class="surname">Ostrander</span></div>

  <div class="wordmark">Halvik Partners Building</div>

  <ul class="contact">
    <li class="license"><span class="label">License:</span> CSLB# 4871306</li>
    <li>
      <svg width="14" height="14" viewBox="0 0 24 24" aria-hidden="true"><path fill="var(--gold)" d="M6.6 10.8a15 15 0 0 0 6.6 6.6l2.2-2.2a1 1 0 0 1 1-.25 11.4 11.4 0 0 0 3.6.57 1 1 0 0 1 1 1V20a1 1 0 0 1-1 1A17 17 0 0 1 3 4a1 1 0 0 1 1-1h3.5a1 1 0 0 1 1 1c0 1.25.2 2.45.57 3.6a1 1 0 0 1-.25 1z"/></svg>
      (619) 482-5537
    </li>
    <li>
      <svg width="14" height="11" viewBox="0 0 24 18" aria-hidden="true"><rect width="24" height="18" rx="2" fill="var(--gold)"/><path d="M1 2l11 8 11-8" stroke="#fff" stroke-width="2" fill="none"/></svg>
      paul@halvikpartners.example
    </li>
  </ul>

  <svg class="footer-bands" width="700" height="90" viewBox="0 0 700 90" aria-hidden="true">
    <polygon points="0,12 330,62 330,90 0,90" fill="var(--navy)"/>
    <polygon points="346,60 700,60 700,90 322,90" fill="var(--gold)"/>
  </svg>
</section>

</body>
</html>
```